Insurance Postcard Design

We need a postcard design for my insurance agency serving a customers in the Silicon Valley area of Northern California. My agency focus is a specialized niche insuring Condominium and Townhouse Homeowner Associations (HOAs) which includes coverage for the HOA Buildings and Directors and Officers. (We do NOT insure autos, single family homes, life or health insurance so please do NOT use any of these themes)
The postcard color theme should be based on the blue with gold/orange stripe color scheme on my website www.kelmorbrant.com where you can also learn more about my specialized insurance business which might be helpful in designing the postcard.
My target customers are HOA Board Members also known as Directors and Officers.
The purpose of the card is to persuade Board Members to call or email me to 1. ask a question or request information, 2. request an HOA insurance evaluation 3. request a quote.
I would like the card Headline
to be: Attention HOA Board Members...
I have included an attached document with some compelling questions and responses that can be used on the postcard Side A and Side B. In designing the cards take into consideration... if postcards are delivered with the Address Side up as sorted by the postal carriers then is the Address Side of the card most likely to be seen first by the customer? If so, then should the question be listed on the Address Side and the answer be listed on the other side?
My attached document also includes a reward as an inducement to call or email me. This inducement should be prominent.
The card should also request a phone call or email multiple times.
I want to use color on both sides of the card.
I want to conduct a split test for results based on card size so please provide identical or nearly identical/comparable designs for both Quillmark Press Small Card Full Bleed size 6.12"x4.12" with Trim Size of 6"x4" and Quillmark Press Oversize Cards Full Bleed size 8.64"x5.59" with Trim Size of 8.52"x5.47".
Both the Small and Oversize card should use the same question and answer and should include the same inducement: a $10 Brewlark Card to everyone who calls or emails. No purchase required. Limited time offer.
After we get the card size results then future designs will include a split test using different inducements/special offers.
Other attached documents include my photo and photo of a Board Meeting that can be included in the design.
Let me know if the three docs: Personal photo, Board Meeting Photo and Headline & Questions did not load. Post a note and include your email and i'll forward any missing docs directly to you.
Reason: Want to provide sufficient time for designers to create postcard designs.
Per Gordon at Quillmark Press the correct card size designers should use is:
Small Card Full Bleed size 6.12" x 4.12" with Trim size 6" x 4"
Oversize Card Full Bleed size 8.64" x 5.59" with Trim size 8.52" x 5.47"
I want to conduct a split test using identical or very similar designs with two size cards to determine best response.
I just uploaded a fresh document dated 9.17.2014 listing Content to be used on the front and back side of the card. Ray Fenwick
Target Market(s)
Board Members aka Directors and Officers for condominium and townhouse homeowner associations. Typical age is 40 to 70. Majority are age 50+. Two out of three board members are women. Board members tend to be conservative. Majority of board members are white/anglo, but growing % is female Indian with lower % female Chinese.
Industry/Entity Type
Insurance
Requirements
Must have
- Try to match my website color scheme. www.kelmorbrant.com I believe shades of blue with orange stripe & buttons gets attention. My web Action buttons are orange.
Include my agency name, Lic. # 7K21364 and website www.kelmorbrant.com
on the card Office address should be included for Return Address: Gregory T. Fenwick Coverage Partners, LLC 3815 Larkfield Blvd. Ste. 207 San Jose, CA 95342
Nice to have
- If there is space on the post card an abbreviated version of the tag line in the orange stripe on my website www.kelmorbrant.com would be good to include: The Best Place to Learn About and Buy HOA Insurance
Should not have
- No insurance themes for auto, boat, motorcycle, single family home, life ins, health ins, financial services. I don't sell any of those products.

```html
<!DOCTYPE html>
<html lang="en">
<head>
<meta charset="utf-8">
<title>HOA Insurance Postcard</title>
<link rel="stylesheet" href="https://fonts.googleapis.com/css2?family=Alfa+Slab+One&family=Francois+One&family=Lato:wght@400;700&family=Bitter:wght@700;800&display=swap">
<style>
  :root{
    --bg:#2b2b2b;
    --blue:#3d6fbd;
    --blue-deep:#1877c8;
    --orange:#f47a2b;
    --green:#8cc21f;
    --white:#ffffff;
    --ink:#1f5fae;
    --dark:#222222;
  }
  *{box-sizing:border-box;margin:0;padding:0}
  html,body{width:885px;height:1200px;overflow:hidden;background:var(--bg)}
  body{position:relative;font-family:"Lato",sans-serif}
  .card{position:absolute;left:62px;width:760px;background:var(--white);overflow:hidden}
  .card--front{top:57px;height:510px}
  .card--back{top:632px;height:513px}
  .card__shapes{position:absolute;inset:0;width:100%;height:100%}
  .abs{position:absolute}

  /* front */
  .agency-title{left:290px;top:26px;width:300px;color:var(--white);font-size:21px;line-height:1.15;text-align:center}
  .burst-text{left:626px;top:14px;width:128px;text-align:center;font-family:"Francois One",sans-serif;color:var(--dark);line-height:1}
  .burst-text .amount{display:block;color:var(--white);font-size:40px}
  .burst-text .label{display:block;font-size:19px;margin-top:2px}
  .headline{left:340px;top:130px;font-family:"Francois One",sans-serif;color:var(--blue);font-size:29px;letter-spacing:.2px}
  .portrait{left:50px;top:40px;width:222px;height:222px;border-radius:50%;background:radial-gradient(circle at 50% 40%,#c9a58e 0,#8f7768 45%,#3f5a3a 100%)}
  .photo{background:linear-gradient(135deg,#d8c8b8,#8f7b6c 60%,#5a4c44);border:3px solid var(--white)}
  .photo--meeting{left:268px;top:184px;width:262px;height:100px}
  .photo--desk{left:541px;top:181px;width:202px;height:104px;background:linear-gradient(135deg,#e6e6e6,#7d7f86 55%,#2b2d34)}
  .questions{left:7px;top:313px;font-family:"Bitter",serif;font-weight:800;color:var(--ink);font-size:11px;line-height:14.6px;white-space:nowrap}
  .questions .plain{color:var(--dark);font-family:"Lato",sans-serif;font-weight:400}
  .fineprint{left:7px;top:443px;width:210px;font-size:10px;line-height:1.3;color:var(--dark)}
  .fineprint .accent{color:var(--ink)}
  .bubble{position:absolute;z-index:2;background:var(--blue);color:var(--white);font-size:14px;border-radius:16px 0 0 16px;padding:0 0 0 16px;display:flex;align-items:center}
  .bubble--one{left:540px;top:307px;width:220px;height:33px;font-size:15px}
  .bubble--two{left:408px;top:353px;width:352px;height:33px;font-size:13px}
  .bubble--three{left:594px;top:401px;width:166px;height:33px;font-size:15px;padding-left:24px}
  .contact-front{left:292px;top:470px;color:var(--white);font-size:22px;display:flex;align-items:center;gap:6px}
  .contact-front svg{flex:none}

  /* back */
  .back-headline{left:16px;top:26px;font-family:"Francois One",sans-serif;color:var(--white);font-size:27px}
  .badge{left:14px;top:78px;width:124px;height:124px;border-radius:50%;background:var(--white);border:5px solid var(--blue-deep);text-align:center;font-family:"Francois One",sans-serif;line-height:1;padding-top:18px}
  .badge .g{display:block;color:var(--green);font-size:20px}
  .badge .fee{display:block;color:var(--dark);font-size:29px;margin:3px 0}
  .badge .g2{display:block;color:var(--green);font-size:14px}
  .offer{left:146px;top:148px;width:240px;font-family:"Bitter",serif;font-weight:800;color:var(--ink);font-size:10.5px;line-height:1.15;text-align:center}
  .pill{position:absolute;background:var(--white);color:var(--dark);border-radius:16px 0 0 16px;display:flex;align-items:center}
  .pill--call{left:166px;top:216px;width:225px;height:30px;font-size:12.5px;padding-left:32px}
  .pill--audit{left:26px;top:262px;width:365px;height:29px;font-size:10.5px;padding-left:12px}
  .pill--web{left:114px;top:309px;width:277px;height:32px;font-family:"Bitter",serif;font-weight:800;color:var(--ink);font-size:16px;padding-left:16px;gap:6px}
  .stamp{left:678px;top:9px;width:76px;height:75px;border:1px solid #555}
  .address-line{position:absolute;left:460px;width:296px;height:1px;background:#999}
  .back-agency{left:420px;top:345px;width:336px;text-align:right;font-family:"Alfa Slab One",serif;color:var(--blue-deep);font-size:20px;line-height:1.25}
  .return-address{left:10px;top:443px;color:var(--white);font-size:18px;line-height:1.3}
  .contact-box{position:absolute;top:458px;height:56px;background:var(--white);border-radius:14px 14px 0 0;display:flex;align-items:center;justify-content:center;gap:6px;color:var(--blue-deep);font-size:16px}
  .contact-box--phone{left:355px;width:153px}
  .contact-box--mail{left:533px;width:238px}
</style>
</head>
<body>

<section class="card card--front" aria-label="Postcard front">
  <svg class="card__shapes" viewBox="0 0 760 510" aria-hidden="true">
    <path d="M0 0H760V40C640 70 470 60 360 95 320 108 300 130 290 150V300H0Z" fill="var(--blue)"/>
    <path d="M300 128C380 90 520 88 640 62 700 48 740 30 760 18" stroke="var(--orange)" stroke-width="6" fill="none"/>
    <path d="M330 112C420 96 560 98 660 82" stroke="var(--orange)" stroke-width="3" fill="none"/>
    <rect x="270" y="175" width="490" height="117" fill="var(--orange)"/>
    <rect x="738" y="292" width="22" height="150" fill="var(--blue)"/>
    <circle cx="161" cy="151" r="128" fill="var(--white)"/>
    <circle cx="161" cy="151" r="118" fill="var(--orange)"/>
    <path d="M220 510C300 440 520 435 760 430V510Z" fill="var(--blue)"/>
    <path d="M180 510C260 450 480 430 760 426" stroke="var(--orange)" stroke-width="7" fill="none"/>
    <polygon fill="var(--green)" points="690,0 700,12 716,4 720,20 738,18 734,34 752,40 740,52 756,64 740,74 752,88 734,92 738,110 720,106 714,122 700,112 690,126 680,112 666,122 660,106 642,110 646,92 628,88 640,74 624,64 640,52 628,40 646,34 642,18 660,20 664,4 680,12"/>
  </svg>

  <div class="abs agency-title">Gregory T. Fenwick Coverage Partners, LLC</div>
  <div class="abs burst-text"><span class="amount">$10</span><span class="label">Brewlark<br>Card</span></div>
  <div class="abs portrait" role="img" aria-label="Portrait photo of the agent"></div>
  <h1 class="abs headline">Attention HOA Board Members...</h1>
  <div class="abs photo photo--meeting" role="img" aria-label="Photo of a board meeting around a table"></div>
  <div class="abs photo photo--desk" role="img" aria-label="Photo of two professionals reviewing documents"></div>

  <p class="abs questions">
    When you get sued...will your Directors &amp; Officerspolicy pay<br>
    Legal Defense Costs?<br>
    Are your personal assets exposed?<br>
    Are current and former directors covered?<br>
    Does your D &amp; O policy exclude Failure to Carry Sufficent<br>
    Insurance?<br>
    Just because your D &amp; O policy &nbsp; is with a Big Name Company, do you think they<br>
    offer the best coverage? <span class="plain">Think again!</span>
  </p>
  <p class="abs fineprint">Did you know...not all D&amp;O policiesuse the same directions.<br><span class="accent">"Who is An Insured"</span> and <span class="accent">"Wrongful Act"</span> can significantly alter coverage.</p>

  <div class="bubble bubble--one">Are you covered? Really?</div>
  <div class="bubble bubble--two">As an HOA Member...are your personal assets exposed?</div>
  <div class="bubble bubble--three">How do you know?</div>

  <div class="abs contact-front">
    <svg width="16" height="18" viewBox="0 0 16 18"><rect x="1" y="1" width="14" height="16" rx="3" fill="var(--white)"/><path d="M5 4c1 0 1.5 2 1 3l-1 1c.6 1.5 1.6 2.6 3 3l1-1c1-.5 3 0 3 1l-1 2c-4 0-8-4-8-8z" fill="var(--blue)"/></svg>
    <span>877-555-0142</span>
    <svg width="22" height="14" viewBox="0 0 22 14" style="margin-left:8px"><rect width="22" height="14" fill="var(--white)"/><path d="M0 0l11 8 11-8" stroke="var(--blue)" stroke-width="1.5" fill="none"/></svg>
    <span>info@kelmorbrant.com</span>
  </div>
</section>

<section class="card card--back" aria-label="Postcard back">
  <svg class="card__shapes" viewBox="0 0 760 513" aria-hidden="true">
    <path d="M0 0H390C385 60 370 90 300 100 200 112 80 90 0 125Z" fill="var(--orange)"/>
    <path d="M0 125C80 90 200 112 300 100 370 90 385 60 390 0V420H0Z" fill="var(--blue-deep)"/>
    <path d="M0 160C60 132 120 118 200 128 280 138 350 140 390 132V205H0Z" fill="var(--white)"/>
    <path d="M0 420C200 420 500 410 760 395V513H0Z" fill="var(--orange)"/>
    <path d="M0 416C220 412 520 405 760 388" stroke="var(--white)" stroke-width="5" fill="none"/>
  </svg>

  <h2 class="abs back-headline">HOA insurance is what we do.</h2>
  <div class="abs badge"><span class="g">Get Your</span><span class="fee">$10 Fee</span><span class="g2">Brewlark Card</span></div>
  <p class="abs offer">When you contact us to get answers to these or other questions or to get a FREE no-obligation HOA Insurance Evaluation.</p>

  <div class="pill pill--call">Don't blow it! Call or email today.</div>
  <div class="pill pill--audit">Based on our recent audits over 40% of HOA insurance is out compliance.</div>
  <div class="pill pill--web">
    <svg width="14" height="14" viewBox="0 0 14 14"><circle cx="7" cy="7" r="6" fill="none" stroke="var(--blue-deep)" stroke-width="1.2"/><ellipse cx="7" cy="7" rx="2.6" ry="6" fill="none" stroke="var(--blue-deep)" stroke-width="1"/><path d="M1 7h12" stroke="var(--blue-deep)"/></svg>
    www.kelmorbrant.com
  </div>

  <div class="abs stamp" aria-label="Stamp area"></div>
  <div class="address-line" style="top:116px"></div>
  <div class="address-line" style="top:143px"></div>
  <div class="address-line" style="top:170px"></div>

  <div class="abs back-agency">Gregory T. Fenwick<br>Coverage Partners, LLC</div>
  <p class="abs return-address">3815 Larkfield Blvd.#207 San Jose,<br>CA 95342 Lic. # 7K21364</p>

  <div class="contact-box contact-box--phone">
    <svg width="15" height="17" viewBox="0 0 16 18"><rect x="1" y="1" width="14" height="16" rx="3" fill="var(--blue-deep)"/><path d="M5 4c1 0 1.5 2 1 3l-1 1c.6 1.5 1.6 2.6 3 3l1-1c1-.5 3 0 3 1l-1 2c-4 0-8-4-8-8z" fill="var(--white)"/></svg>
    877-555-0142
  </div>
  <div class="contact-box contact-box--mail">
    <svg width="22" height="14" viewBox="0 0 22 14"><rect width="22" height="14" fill="var(--blue-deep)"/><path d="M0 0l11 8 11-8" stroke="var(--white)" stroke-width="1.5" fill="none"/></svg>
    info@kelmorbrant.com
  </div>
</section>

</body>
</html>
```